Vireo Tramvex 2025

We must establish a distinct identity for our trade show stand. This includes designing artwork intended for printing on a wall measuring 2,1 x 4 meters and another wall measuring 2,1 x 2 meters. Central to the 2,1 x 4-meter wall, we will position a 55-inch television. I will provide some artistic references and sketches of our stand for your review and as a foundational basis for the design process.

The idea is to place our services listed in file draft branding into the 2,1 X 4 wall with the identity presented in the file 01 Apresentacao - Vireo IDV

```html
<!DOCTYPE html>
<html lang="es">
<head>
<meta charset="utf-8">
<title>Vireo Tramvex 2025 – Stand</title>
<link rel="stylesheet" href="https://fonts.googleapis.com/css2?family=Poppins:wght@400;500;700;800&display=swap">
<style>
  :root{
    --ink:#0a0a0b;
    --paper:#ffffff;
    --red:#e3120b;
    --red-deep:#a8070a;
    --land:#e4e4e4;
    --green:#3fd61b;
    --text:#f2f2f2;
    --line:#cfcfcf;
  }
  *{margin:0;padding:0;box-sizing:border-box}
  html,body{width:1200px;height:360px;overflow:hidden;background:var(--paper)}
  body{position:relative;font-family:'Poppins',sans-serif;color:var(--text)}

  .wall{position:absolute;background:var(--ink);outline:1px solid #d8d8d8}
  .wall--map{left:141px;top:13px;width:323px;height:338px;overflow:hidden}
  .wall--main{left:467px;top:12px;width:646px;height:339px;overflow:hidden}

  .map-art{position:absolute;inset:0;
    background:radial-gradient(ellipse 55% 60% at 50% 50%, #1c1c1e 0%, #121213 60%, var(--ink) 100%)}
  .map-marks{position:absolute;inset:0;width:323px;height:338px}
  .country{position:absolute;background:var(--red);color:var(--paper);
    font-size:5.5px;font-weight:500;line-height:7px;padding:0 2px;white-space:nowrap}

  .hero-photo{position:absolute;inset:0;
    background:radial-gradient(ellipse 30% 55% at 25% 55%, #3a4457 0%, #1b2130 55%, transparent 80%),
               radial-gradient(ellipse 30% 25% at 28% 0%, #8fa2b8 0%, #2b3445 40%, transparent 75%),
               linear-gradient(180deg,#141a24 0%,#0c0f15 100%)}
  .screen{position:absolute;left:227px;top:64px;width:195px;height:110px;background:var(--paper)}

  .brand{position:absolute;left:460px;top:10px;display:flex;align-items:flex-end;gap:5px}
  .brand__name{font-weight:800;font-size:48px;line-height:1;color:var(--paper);letter-spacing:-1px}
  .brand__dot{width:6px;height:6px;border-radius:50%;background:var(--red);margin-bottom:6px}

  .tagline{position:absolute;left:460px;top:84px;font-weight:800;font-size:22px;line-height:23px;color:var(--paper)}
  .tagline__rec{display:inline-block;width:12px;height:12px;border-radius:50%;background:var(--red);margin-left:4px;vertical-align:-1px}
  .tagline__play{display:inline-block;width:0;height:0;border-left:13px solid var(--green);border-top:7px solid transparent;border-bottom:7px solid transparent;margin-left:2px;vertical-align:-1px}

  .services{position:absolute;left:0;top:0;width:646px;height:339px}
  .service-label{position:absolute;font-size:9px;line-height:9.5px;color:var(--text);font-weight:400}
  .service-label--right{text-align:right}
</style>
</head>
<body>

<section class="wall wall--map" aria-label="Presencia regional">
  <div class="map-art" role="img" aria-label="Mapa de América Latina en gris claro sobre fondo negro"></div>

  <svg class="map-marks" viewBox="0 0 323 338" aria-hidden="true">
    <defs>
      <g id="pin">
        <path d="M0 0 L-2 -3.5 A2.3 2.3 0 1 1 2 -3.5 Z" fill="var(--red)" stroke="var(--red-deep)" stroke-width="0.4"/>
        <circle cx="0" cy="-4.6" r="0.8" fill="var(--paper)"/>
      </g>
    </defs>
    <g class="leader" fill="none" stroke="var(--line)" stroke-width="0.5">
      <polyline points="14,62 76,62 82.5,64.7"/>
      <polyline points="28,76 102,76 108,78"/>
      <polyline points="45,95 107,95 113,82.5"/>
      <polyline points="57,108 122,108 128,94"/>
      <polyline points="60,117 130,117 136,100"/>
      <polyline points="86,127 148,127 154,112"/>
      <polyline points="71,140 136,140 142,126"/>
      <polyline points="84,152 146,152 152,154"/>
      <polyline points="114,179 176,179 182,181"/>
      <polyline points="93,242 155,242 161,243"/>
      <polyline points="212,76 126,76 120,79"/>
      <polyline points="212,86 131,86 125,86"/>
      <polyline points="314,182 250,182 244,185"/>
      <polyline points="294,195 211,195 205,197"/>
      <polyline points="281,225 216,225 210,228"/>
      <polyline points="239,255 175,255 169,257"/>
    </g>
    <g class="pins">
      <use href="#pin" x="82.5" y="67"/>
      <use href="#pin" x="108" y="80"/>
      <use href="#pin" x="113" y="84.5"/>
      <use href="#pin" x="128" y="96"/>
      <use href="#pin" x="136" y="102"/>
      <use href="#pin" x="154" y="114"/>
      <use href="#pin" x="142" y="128"/>
      <use href="#pin" x="152" y="156"/>
      <use href="#pin" x="182" y="183"/>
      <use href="#pin" x="161" y="245"/>
      <use href="#pin" x="120" y="81"/>
      <use href="#pin" x="125" y="88"/>
      <use href="#pin" x="244" y="187"/>
      <use href="#pin" x="205" y="199"/>
      <use href="#pin" x="210" y="230"/>
      <use href="#pin" x="169" y="259"/>
    </g>
  </svg>

  <span class="country" style="left:14px;top:55px">México</span>
  <span class="country" style="left:28px;top:69px">Guatemala</span>
  <span class="country" style="left:45px;top:88px">El Salvador</span>
  <span class="country" style="left:57px;top:101px">Costa Rica</span>
  <span class="country" style="left:60px;top:110px">Panamá</span>
  <span class="country" style="left:86px;top:120px">Colombia</span>
  <span class="country" style="left:71px;top:133px">Ecuador</span>
  <span class="country" style="left:84px;top:145px">Perú</span>
  <span class="country" style="left:114px;top:172px">Bolivia</span>
  <span class="country" style="left:93px;top:235px">Chile</span>
  <span class="country" style="left:183px;top:69px">Honduras</span>
  <span class="country" style="left:181px;top:79px">Nicaragua</span>
  <span class="country" style="left:297px;top:175px">Brasil</span>
  <span class="country" style="left:265px;top:188px">Paraguay</span>
  <span class="country" style="left:253px;top:218px">Uruguay</span>
  <span class="country" style="left:210px;top:248px">Argentina</span>
</section>

<section class="wall wall--main" aria-label="Servicios">
  <div class="hero-photo" role="img" aria-label="Fotografía de un espectador en una sala de cine, iluminado por el proyector"></div>
  <div class="screen" aria-label="Espacio para televisor"></div>

  <div class="brand">
    <span class="brand__name">Vireo</span>
    <span class="brand__dot"></span>
  </div>

  <h1 class="tagline">End2End<br>Solutions<br>From Record<br>to Play<span class="tagline__rec"></span><span class="tagline__play"></span></h1>

  <svg class="services" viewBox="0 0 646 339" aria-hidden="true">
    <g fill="none" stroke="var(--line)" stroke-width="0.7" stroke-dasharray="1.5 1.5">
      <path d="M138 258 V232 H169"/>
      <path d="M186 249 V278 H220"/>
      <path d="M237 259 V232 H270"/>
      <path d="M287 249 V278 H321"/>
      <path d="M338 259 V232 H372"/>
      <path d="M389 249 V278 H423"/>
      <path d="M440 259 V232 H475"/>
      <path d="M492 249 V278 H528"/>
    </g>
    <g fill="var(--red)" stroke="var(--paper)" stroke-width="1.6">
      <circle cx="186" cy="232" r="16.5"/>
      <circle cx="287" cy="232" r="16.5"/>
      <circle cx="389" cy="232" r="16.5"/>
      <circle cx="492" cy="233" r="16.5"/>
      <circle cx="138" cy="275" r="16.5"/>
      <circle cx="237" cy="276" r="16.5"/>
      <circle cx="338" cy="276" r="16.5"/>
      <circle cx="440" cy="276" r="16.5"/>
      <circle cx="545" cy="278" r="16.5"/>
    </g>
    <g fill="none" stroke="var(--paper)" stroke-width="1" stroke-linejoin="round">
      <rect x="179" y="226" width="14" height="10" rx="1"/><path d="M186 230 V240 M183 240 H189"/>
      <rect x="283" y="224" width="8" height="12" rx="1"/><circle cx="287" cy="229" r="2"/><path d="M287 236 V240"/>
      <path d="M382 226 h13 v8 h-4 l-3 3 v-3 h-6 z"/><path d="M385 237 v2 h8 l2 2 v-6"/>
      <circle cx="492" cy="233" r="7"/><circle cx="489" cy="231" r="1.8"/><circle cx="495" cy="231" r="1.8"/><circle cx="492" cy="236" r="1.8"/>
      <rect x="131" y="272" width="14" height="9" rx="1"/><path d="M131 272 l13-4 1 3"/>
      <rect x="230" y="270" width="14" height="11"/><path d="M231 279 l4-4 3 3 3-5 3 4"/>
      <rect x="331" y="270" width="14" height="11" rx="1"/><path d="M333 279 l4-4 3 3 3-3 2 2"/>
      <rect x="433" y="269" width="14" height="9"/><path d="M433 281 h14 M435 283 h10"/>
      <rect x="538" y="271" width="14" height="11" rx="1"/><path d="M546 279 h-5 l2-2 m-2 2 l2 2"/>
    </g>
  </svg>

  <span class="service-label service-label--right" style="right:479px;top:221px">Editorial</span>
  <span class="service-label" style="left:235px;top:213px">Post<br>Sonido</span>
  <span class="service-label service-label--right" style="right:277px;top:221px">Doblaje</span>
  <span class="service-label" style="left:430px;top:211px">Laboratorio<br>Fílmico</span>
  <span class="service-label service-label--right" style="right:528px;top:269px">On-Set</span>
  <span class="service-label" style="left:185px;top:280px">Post<br>Imagen</span>
  <span class="service-label" style="left:290px;top:284px">VFX</span>
  <span class="service-label" style="left:387px;top:283px">Cinema<br>Digital</span>
  <span class="service-label service-label--right" style="right:120px;top:283px">Distribución</span>
</section>

</body>
</html>
```